KORVEN-DALE OUTFITTERS e-Commerce product sales website

e-Commerce product sales website. See eBay storefront below. Military, Emergency, Survival, Rescue, First Aid, Trauma. Hunting, Camping, Hiking, Backpacking gear and equipment.

https://www.tradevine-market.example/shop/korvendaleoutfitters

Be Prepared For:

- SHTF
- Hurricane
- Tornado
- Flooding
- Evacuation
- Earthquake
- Blizzard
- Wild Fire
- Stranded Auto
- Traffic Shutdown
- Civil Unrest
- Lost Hiker
- Lost Boater
- Grid Down
- Pandemic
- Zombie Apocalypse

KORVEN-DALE OUTFITTERS: Gear Up When It Matters Most

At KORVEN-DALE OUTFITTERS, we understand that when you're most vulnerable, you need reliable gear that won’t let you down. Built on a foundation of military survival expertise, we offer high-quality tactical gear designed for real-world challenges—not generic, one-size-fits-all options.

What We Offer:

•Premium Tactical Gear: Our selection is curated for durability and functionality. Forget cheap imitations; we provide real solutions that stand up to the toughest conditions.

•Fresh MREs & Emergency Bars: No prep, no hassle. Our meals are ready to eat and designed for convenience, so you can focus on what matters when disaster strikes.

•Rigorous Testing: Each product undergoes personal testing and vetting to ensure it meets our high standards. We only offer gear that we trust with our own lives.

Why Choose KORVEN-DALE?

When it comes to survival, don’t settle for disposable, unreliable equipment. Choose KORVEN-DALE for gear that will perform when you need it most. Prepare for the unexpected and ensure you have the best.

Get KORVEN-DALE…..Because…..Trails Bite…...

Target Market(s)

Survival, Emergency, First Responder, Prepare, Military, First Aid, Disaster Preparedness, Camping, Hiking, Backpacking, Adventurer

Industry/Entity Type

Survival, Emergency, First Responder, Prepper, Military, First Aid, Disaster Preparedness

Coding

Coded - Design and coding required

Number of Pages Required

5+ page

Font styles to use
Other font styles liked:
• Octin Stencil

Colors
EE7325
F08F49
F5BC92
FAE3D3
FDF4ED

Requirements
Must have
• e-commerce, sales and credit card acceptance. Drop down options on products for sizes, colors and product options. Ability to update products, features and photos.
Nice to have
• Drop down options on products for sizes, colors and product options.
Should not have
• Personal photos

```html
<!DOCTYPE html>
<html lang="en">
<head>
<meta charset="utf-8">
<title>KORVEN-DALE OUTFITTERS</title>
<link href="https://fonts.googleapis.com/css2?family=Saira+Stencil+One&family=Oswald:wght@400;500;600;700&family=Poppins:wght@400;500;600;700&display=swap" rel="stylesheet">
<style>
:root{
  --orange:#EE7325;
  --orange-2:#F08F49;
  --orange-3:#F5BC92;
  --orange-4:#FAE3D3;
  --orange-5:#FDF4ED;
  --ink:#1a1a1a;
  --dark:#101010;
  --dark-2:#1c1c1c;
  --grey:#8a8a8a;
  --hex:#9a9a9a;
  --white:#ffffff;
}
*{box-sizing:border-box;margin:0;padding:0}
html,body{width:1200px;height:4332px;overflow:hidden}
body{font-family:'Poppins',sans-serif;color:var(--ink);background:var(--white);position:relative}
.abs{position:absolute}
.stencil{font-family:'Saira Stencil One',sans-serif}
.heading{font-family:'Oswald',sans-serif;font-weight:600;text-transform:uppercase}
.accent{color:var(--orange)}
.btn{display:inline-block;background:var(--orange);color:var(--white);font:600 11px 'Poppins',sans-serif;text-transform:uppercase;padding:9px 20px;letter-spacing:.5px}

/* header */
.site-header{top:0;left:0;width:1200px;height:112px;background:var(--white);border-bottom:1px solid #eee}
.topbar{top:10px;left:56px;font-size:11px;color:#444;display:flex;gap:26px;align-items:center}
.topbar span{display:flex;gap:6px;align-items:center}
.social-top{top:10px;right:56px;display:flex;gap:10px}
.social-top i{width:14px;height:14px;border-radius:50%;background:#333;display:block}
.brand{top:40px;left:112px;display:flex;align-items:center;gap:10px}
.brand-square{width:28px;height:28px;background:var(--orange)}
.brand-name{font:700 15px 'Oswald',sans-serif;letter-spacing:1px;color:var(--ink)}
.main-nav{top:62px;left:372px;display:flex;gap:28px;font-size:11px;font-weight:500;text-transform:uppercase;color:#333}
.main-nav .active{color:var(--orange)}
.nav-tools{top:60px;left:880px;display:flex;gap:14px;align-items:center}
.nav-tools i{width:12px;height:12px;border:2px solid #333;border-radius:50%;display:block}
.contact-btn{top:54px;right:64px;padding:8px 18px}

/* hero */
.hero{top:112px;left:0;width:1200px;height:640px;background:radial-gradient(ellipse at 25% 45%,#6a4b2c 0%,#2d2a22 40%,#141412 80%),#141412}
.hero-side{top:420px;left:-60px;transform:rotate(-90deg);font:600 22px 'Oswald',sans-serif;letter-spacing:4px;color:rgba(255,255,255,.35)}
.hero-mark{top:250px;left:150px;display:flex;align-items:center;gap:18px}
.hero-mark .sq{width:90px;height:90px;background:var(--orange)}
.hero-mark .nm{font:700 34px 'Oswald',sans-serif;color:var(--white);line-height:1.1;width:260px}
.hero-title{top:228px;left:592px;color:var(--white);font-size:82px;line-height:.98}
.hero-tag{top:420px;left:596px;font:500 30px 'Oswald',sans-serif;color:var(--white);letter-spacing:1px}

/* categories */
.section-title{width:1200px;text-align:center;font-size:44px;left:0}
.cat-row{top:880px;left:0;width:1200px}
.cat{position:absolute;width:140px;text-align:center}
.cat svg{display:block;margin:0 auto}
.cat p{margin-top:14px;font-size:13px;font-weight:500;text-transform:uppercase}
.cat-arrow{top:918px}
.view-cats{top:1104px;left:540px;font-size:9px;font-weight:600;color:var(--grey);border-bottom:2px solid var(--orange);padding:2px 10px}

/* about */
.about-kicker{top:1212px;left:88px;font-size:24px}
.about-title{top:1250px;left:88px;font-size:44px;line-height:1.05}
.about-mark{top:1220px;left:480px;display:flex;align-items:center;gap:14px}
.about-mark .sq{width:60px;height:60px;background:var(--orange)}
.about-mark .nm{font:700 22px 'Oswald',sans-serif;color:var(--orange);width:170px;line-height:1.1}
.about-copy{top:1214px;left:780px;width:330px;font-size:12px;line-height:1.6;color:#333}
.about-btn{top:1318px;left:780px}

/* offer */
.offer{top:1500px;left:0;width:1200px;height:500px;background:radial-gradient(ellipse at 50% 60%,#2a2a2a,#0c0c0c 75%)}
.offer .section-title{top:60px;color:var(--white)}
.offer-card{position:absolute;top:124px;width:284px;height:350px;clip-path:polygon(50% 0,100% 22%,100% 78%,50% 100%,0 78%,0 22%);background:var(--white);text-align:center;padding:70px 34px 0}
.offer-card.featured{background:var(--orange);color:var(--white)}
.offer-card .badge{width:38px;height:38px;margin:0 auto 14px;background:var(--orange)}
.offer-card.featured .badge{background:var(--white)}
.offer-card h3{font-size:13px;font-weight:600;text-transform:uppercase;margin-bottom:10px}
.offer-card p{font-size:11px;line-height:1.55}
.offer-card .more{margin-top:14px;font-size:10px;font-weight:600;color:var(--orange);text-transform:uppercase}
.offer-card.featured .more{color:var(--white)}

/* products */
.product{position:absolute;overflow:hidden}
.product .photo{position:absolute;inset:0}
.product .caption{position:absolute;left:24px;color:var(--white);text-transform:uppercase}
.product .caption h4{font-size:14px;font-weight:600;line-height:1.35}
.product .caption b{display:block;font:600 26px 'Oswald',sans-serif;margin-top:6px}
.view-products{top:2966px;left:530px;font-size:10px;background:var(--ink)}

/* deal */
.deal{top:3080px;left:0;width:1200px;height:240px;background:linear-gradient(90deg,#0d0d0d 0%,#2a2520 50%,#0d0d0d 100%)}
.deal-tag{top:40px;left:128px;background:var(--white);color:var(--ink);font-size:9px;font-weight:600;padding:4px 14px;text-transform:uppercase}
.deal-title{top:88px;left:128px;color:var(--white);font:600 38px 'Oswald',sans-serif;line-height:1.2}
.timer{top:78px;left:640px;display:flex;gap:18px}
.timer div{width:92px;height:92px;border:2px solid var(--orange);border-radius:14px;background:rgba(0,0,0,.6);color:var(--white);text-align:center;padding-top:12px}
.timer b{display:block;font:600 38px 'Oswald',sans-serif;line-height:1}
.timer span{font-size:10px;font-weight:600;letter-spacing:1px}
.timer em{color:var(--white);font:600 36px 'Oswald',sans-serif;font-style:normal;align-self:center}

/* why */
.why-mark{top:3420px;left:180px;display:flex;align-items:center;gap:20px}
.why-mark .sq{width:110px;height:110px;background:var(--orange)}
.why-mark .nm{font:700 32px 'Oswald',sans-serif;color:var(--orange);width:220px;line-height:1.1}
.why-title{top:3464px;left:608px;font-size:40px}
.why-copy{top:3530px;left:608px;width:470px;font-size:13px;line-height:1.6;color:#333}

/* footer */
.footer{top:3740px;left:0;width:1200px;height:592px;background:linear-gradient(180deg,#1a1a1a,#0a0a0a)}
.footer-brand{top:100px;left:0;width:1200px;display:flex;justify-content:center;align-items:center;gap:14px}
.footer-brand .sq{width:44px;height:44px;background:var(--orange)}
.footer-brand .nm{font:700 26px 'Oswald',sans-serif;color:var(--white);letter-spacing:1px}
.footer-col{top:228px;color:var(--white)}
.footer-col h5{font:500 22px 'Oswald',sans-serif;text-transform:uppercase;margin-bottom:14px;border-bottom:2px solid var(--orange);padding-bottom:8px}
.footer-col ul{list-style:none;font-size:12px;line-height:2.05;color:#ddd}
.contact-item{display:flex;gap:12px;margin-bottom:16px;font-size:12px;line-height:1.5;color:#ddd}
.contact-item .ico{width:18px;height:18px;border-radius:50%;background:var(--orange);flex:none;margin-top:2px}
.contact-item b{display:block;color:var(--white);font-size:11px;text-transform:uppercase}
.newsletter{display:flex;align-items:center;width:360px;height:40px;background:var(--white);border-radius:20px;padding:0 6px 0 18px;font-size:12px;color:#888;justify-content:space-between}
.newsletter i{width:30px;height:30px;border-radius:50%;background:var(--orange);display:block}
.footer-social{display:flex;gap:12px;margin-top:20px}
.footer-social i{width:32px;height:32px;border-radius:50%;background:var(--orange);display:block}
.copyright{bottom:0;left:0;width:1200px;height:40px;background:#000;color:#ccc;text-align:center;font-size:11px;line-height:40px;letter-spacing:.5px}
.to-top{bottom:52px;right:40px;width:36px;height:36px;border-radius:50%;background:var(--orange)}
</style>
</head>
<body>

<header class="site-header abs">
  <div class="topbar abs">
    <span><svg width="11" height="11" viewBox="0 0 24 24"><path fill="#EE7325" d="M6.6 10.8a15 15 0 006.6 6.6l2.2-2.2a1 1 0 011-.25 11 11 0 003.6.6 1 1 0 011 1V20a1 1 0 01-1 1A17 17 0 013 4a1 1 0 011-1h3.5a1 1 0 011 1 11 11 0 00.6 3.6 1 1 0 01-.25 1z"/></svg>(555) 014 2290</span>
    <span><svg width="12" height="10" viewBox="0 0 24 18"><rect x="1" y="1" width="22" height="16" fill="none" stroke="#EE7325" stroke-width="2"/><path d="M1 1l11 9 11-9" fill="none" stroke="#EE7325" stroke-width="2"/></svg>hello@korvendale.example</span>
  </div>
  <div class="social-top abs"><i></i><i></i><i></i><i></i><i></i></div>
  <div class="brand abs"><div class="brand-square"></div><div class="brand-name">KORVEN-DALE OUTFITTERS</div></div>
  <nav class="main-nav abs">
    <span class="active">Home</span><span>Products</span><span>Categories</span><span>Sale</span><span>About Us</span><span>Why Choose Us</span><span>Feedback</span>
  </nav>
  <div class="nav-tools abs"><i></i><i></i></div>
  <span class="btn contact-btn abs">Contact Us</span>
</header>

<section class="hero abs" role="img" aria-label="Moody photo of an outdoor survival scene with a soldier in tactical gear and warm orange light">
  <div class="hero-side abs">KORVENDALEOUTFITTERS.EXAMPLE</div>
  <div class="hero-mark abs"><div class="sq"></div><div class="nm">KORVEN-DALE OUTFITTERS</div></div>
  <h1 class="hero-title stencil abs">KORVEN-DALE<br>OUTFIT<span class="accent">TERS</span></h1>
  <p class="hero-tag abs">GEAR UP WHEN IT MATTERS MOST</p>
</section>

<h2 class="section-title heading abs" style="top:784px">Featured <span class="accent">Categories</span></h2>
<svg class="cat-arrow abs" style="left:84px" width="22" height="34" viewBox="0 0 22 34"><path d="M20 2L3 17l17 15z" fill="#8a8a8a"/></svg>
<svg class="cat-arrow abs" style="left:1094px" width="22" height="34" viewBox="0 0 22 34"><path d="M2 2l17 15L2 32z" fill="#EE7325"/></svg>
<div class="cat-row abs">
  <div class="cat" style="left:162px">
    <svg width="120" height="132" viewBox="0 0 120 132"><polygon points="60,2 116,34 116,98 60,130 4,98 4,34" fill="#9a9a9a"/><circle cx="60" cy="66" r="26" fill="none" stroke="#fff" stroke-width="6"/><path d="M60 44v44M46 60h28" stroke="#fff" stroke-width="6"/></svg>
    <p>Survival</p>
  </div>
  <div class="cat" style="left:338px">
    <svg width="120" height="132" viewBox="0 0 120 132"><polygon points="60,2 116,34 116,98 60,130 4,98 4,34" fill="#9a9a9a"/><circle cx="60" cy="66" r="8" fill="#fff"/><circle cx="60" cy="46" r="12" fill="none" stroke="#fff" stroke-width="6"/><circle cx="43" cy="76" r="12" fill="none" stroke="#fff" stroke-width="6"/><circle cx="77" cy="76" r="12" fill="none" stroke="#fff" stroke-width="6"/></svg>
    <p>Emergency</p>
  </div>
  <div class="cat" style="left:514px">
    <svg width="120" height="132" viewBox="0 0 120 132"><polygon points="60,2 116,34 116,98 60,130 4,98 4,34" fill="#EE7325"/><path d="M60 94L32 66a16 16 0 0128-18 16 16 0 0128 18z" fill="#fff"/><path d="M60 56v22M49 67h22" stroke="#EE7325" stroke-width="6"/></svg>
    <p>First Aid</p>
  </div>
  <div class="cat" style="left:690px">
    <svg width="120" height="132" viewBox="0 0 120 132"><polygon points="60,2 116,34 116,98 60,130 4,98 4,34" fill="#9a9a9a"/><path d="M36 92L84 40" stroke="#fff" stroke-width="8" stroke-linecap="round"/><path d="M50 70l10 12" stroke="#fff" stroke-width="6"/></svg>
    <p>Tactical</p>
  </div>
  <div class="cat" style="left:866px">
    <svg width="120" height="132" viewBox="0 0 120 132"><polygon points="60,2 116,34 116,98 60,130 4,98 4,34" fill="#9a9a9a"/><path d="M30 66l30-26 30 26" fill="none" stroke="#fff" stroke-width="6"/><path d="M38 62v28h44V62" fill="#fff"/><rect x="54" y="74" width="12" height="16" fill="#9a9a9a"/></svg>
    <p>Shelter</p>
  </div>
</div>
<div class="view-cats abs">VIEW ALL CATEGORIES</div>

<p class="about-kicker heading abs">About <span class="accent">Us</span></p>
<h2 class="about-title heading abs">At <span class="accent">Korven-Dale</span><br><span class="accent">Outfitters</span></h2>
<div class="about-mark abs"><div class="sq"></div><div class="nm">KORVEN-DALE OUTFITTERS</div></div>
<p class="about-copy abs">We understand that when you're most vulnerable, you need reliable gear that won't let you down. Built on a foundation of military survival expertise, we offer</p>
<span class="btn about-btn abs">Read More</span>

<section class="offer abs">
  <h2 class="section-title heading abs">What We <span class="accent">Offer</span></h2>
  <div class="offer-card" style="left:196px">
    <div class="badge"></div>
    <h3>Premium Tactical Gear</h3>
    <p>Our selection is curated for durability and functionality. Forget cheap imitations.</p>
    <div class="more">Read More &rarr;</div>
  </div>
  <div class="offer-card featured" style="left:458px">
    <div class="badge"></div>
    <h3>Fresh MREs &amp; Emergency Bars</h3>
    <p>No prep, no hassle. Our meals are ready to eat and designed for convenience.</p>
    <div class="more">Read More &rarr;</div>
  </div>
  <div class="offer-card" style="left:720px">
    <div class="badge"></div>
    <h3>Rigorous Testing</h3>
    <p>Each product undergoes personal testing and vetting to ensure it meets our high standards.</p>
    <div class="more">Read More &rarr;</div>
  </div>
</section>

<h2 class="section-title heading abs" style="top:2100px">Featured <span class="accent">Products</span></h2>

<div class="product" style="top:2196px;left:88px;width:504px;height:342px">
  <div class="photo" role="img" aria-label="Photo of a tan military tactical backpack" style="background:linear-gradient(135deg,#6b5a45,#3b3128 60%,#1f1a15)"></div>
  <div class="caption" style="top:140px"><h4>40L Military Tactical<br>Backpack Molle Bag<br>Rucksack / Assault Pack</h4><b>$27.50</b></div>
</div>
<div class="product" style="top:2560px;left:88px;width:504px;height:392px">
  <div class="photo" role="img" aria-label="Photo of a green survival tube tent pitched on grass" style="background:linear-gradient(160deg,#8ea08a,#4d6a55 55%,#2a3a2c)"></div>
  <div class="caption" style="top:150px"><h4>Emergency Tube Tent<br>Survival Hiking Camping<br>Shelter Outdoor Portable</h4><b>$37.50</b></div>
</div>
<div class="product" style="top:2196px;left:608px;width:504px;height:756px">
  <div class="photo" role="img" aria-label="Photo of a red camping hammock strung between trees in a forest" style="background:radial-gradient(ellipse at 55% 48%,#c9402a 0%,#7a4a2a 22%,#4a5a38 55%,#2c3a24)"></div>
  <div class="caption" style="top:600px;left:40px"><h4>Camping Hammock with<br>Mosquito Net / Rainfly<br>Cover Tarp Fall</h4><b>$42.50</b></div>
</div>
<span class="btn view-products abs">View All Products</span>

<section class="deal abs" role="img" aria-label="Dark background photo of survival kit gear">
  <div class="deal-tag abs">Hot Deal</div>
  <h2 class="deal-title abs">15% OFF ON SURVIVAL KIT<br>LIMITED OFFER! NOW: <span class="accent">$60.59</span></h2>
  <div class="timer abs">
    <div><b>25</b><span>DAYS</span></div><em>:</em>
    <div><b>05</b><span>HRS</span></div><em>:</em>
    <div><b>35</b><span>MIN</span></div><em>:</em>
    <div><b>35</b><span>SEC</span></div>
  </div>
</section>

<div class="why-mark abs"><div class="sq"></div><div class="nm">KORVEN-DALE OUTFITTERS</div></div>
<h2 class="why-title heading abs">Why Choose <span class="accent">Korven-Dale?</span></h2>
<p class="why-copy abs">When it comes to survival, don't settle for disposable, unreliable equipment. Choose KORVEN-DALE for gear that will perform when you need it most. Prepare for the unexpected and ensure you have the best.</p>

<footer class="footer abs">
  <div class="footer-brand abs"><div class="sq"></div><div class="nm">KORVEN-DALE OUTFITTERS</div></div>
  <div class="footer-col abs" style="left:88px;width:200px">
    <h5>Quick Link</h5>
    <ul><li>Home</li><li>Shop</li><li>Categories</li><li>Sale</li><li>About Us</li><li>Why Choose Us</li><li>Feedback</li><li>Contact Us</li></ul>
  </div>
  <div class="footer-col abs" style="left:420px;width:260px">
    <h5>Contact Us</h5>
    <div class="contact-item"><i class="ico"></i><div><b>Address</b>41 Ridgeback Lane,<br>Stonebrook 55021</div></div>
    <div class="contact-item"><i class="ico"></i><div><b>Email</b>orders@korvendale.example</div></div>
    <div class="contact-item"><i class="ico"></i><div><b>Phone</b>+00 555-014-229</div></div>
  </div>
  <div class="footer-col abs" style="left:732px;width:380px">
    <h5>Subscribe Our Newsletter</h5>
    <div class="newsletter">Enter Your Email<i></i></div>
    <div class="footer-social"><i></i><i></i><i></i><i></i></div>
  </div>
  <div class="to-top abs"></div>
  <div class="copyright abs">COPYRIGHT 2024 KORVEN-DALE OUTFITTERS. ALL RIGHTS RESERVED</div>
</footer>

</body>
</html>
```